New Business Card Design Project

possibly double-sided card, with one side in color. leaves, a tree branch, or a tree of life, like laurel, olive, pine ... or a seed that grows. visual discreet and stylized or naive. no photo. no human silhouette Modern Typo possibly rounded corners matte paper, no selective varnish, neither gold nor silver English brief Double sided business card, with eventually a single colored side. Leaves, a tree branch or a tree of life, laurel, olive tree, pine tree ... or a growing seed. The design has to be discreet and stylized or naive. No human silhouettes Modern made Possibly rounded corners Matte paper, no selective varnish, no gold, no silver
Updates

I really prefer toned or subtles tones, Bluish / greenwich gray, verdigris ... Elegant and discreet colors Write "HUMANISTIC HYPNOTHERAPY, SYMBOLIC THERAPY" on 2 lines and on One side only (not with the name and address) Not use pictogram (such , address...)

Contact Information for Business Card

Hypnothérapie humaniste
Thérapie symbolique

Marianne Lebrodel
Hypnothérapeute
06 48 17 20 85
47 rue des Tilleuls-Brunoy, 33710 Morvalle
cabinet.lebrodel@velmoria.fr

Colors
33b8a4
3176b5

Requirements
Must have
• sober, elegant and refined card Sober design, elegant, plain
Nice to have
• desired colors: gray, blue-gis, greyish, khaki ... Desired colors: gray, blue-gray, grayish green, khaki, ...
Should not have
• gaudy colors, bright greens no bright gold neon colors

```html
<!DOCTYPE html>
<html lang="fr">
<head>
<meta charset="utf-8">
<title>Marianne Lebrodel – Hypnothérapeute</title>
<link rel="stylesheet" href="https://fonts.googleapis.com/css2?family=Cinzel:wght@400&family=Lato:wght@400&display=swap">
<style>
  :root {
    --bg: #a6a6a6;
    --card-white: #ffffff;
    --ink: #1f1f1f;
    --ink-soft: #444a4d;
    --teal: #2a9c9c;
    --back-top: #3d7ba6;
    --back-bottom: #6cbaac;
    --back-text: #f4f8f8;
    --motif-light: rgba(140, 200, 200, 0.30);
    --motif-fade: rgba(140, 200, 200, 0.08);
  }
  * { margin: 0; padding: 0; box-sizing: border-box; }
  html, body {
    width: 1200px;
    height: 960px;
    overflow: hidden;
    background: var(--bg);
  }
  .canvas {
    position: relative;
    width: 1200px;
    height: 960px;
  }
  .card {
    position: absolute;
    left: 296px;
    width: 609px;
    height: 358px;
    border-radius: 34px;
    overflow: hidden;
  }
  .card--front {
    top: 81px;
    background: var(--card-white);
  }
  .card--back {
    top: 464px;
    background: linear-gradient(180deg, var(--back-top) 0%, var(--back-bottom) 100%);
  }
  .holder {
    position: absolute;
    left: 31px;
    top: 30px;
  }
  .holder__name {
    font-family: "Cinzel", "Times New Roman", serif;
    font-weight: 400;
    font-size: 24px;
    letter-spacing: 0.5px;
    color: var(--ink);
    line-height: 1.1;
  }
  .holder__role {
    font-family: "Lato", Arial, sans-serif;
    font-size: 15px;
    color: var(--teal);
    margin-top: 3px;
    letter-spacing: 0.2px;
  }
  .contact {
    position: absolute;
    left: 55px;
    top: 256px;
    list-style: none;
    font-family: "Lato", Arial, sans-serif;
    font-size: 15.5px;
    color: var(--ink-soft);
  }
  .contact__item {
    display: flex;
    align-items: center;
    height: 25.5px;
  }
  .tree-motif {
    position: absolute;
    left: 135px;
    top: 0;
    width: 347px;
    height: 358px;
    border-radius: 48% 48% 40% 40% / 36% 36% 20% 20%;
    background: linear-gradient(180deg, var(--motif-light) 0%, var(--motif-fade) 55%, var(--motif-light) 100%);
  }
  .practice {
    position: absolute;
    left: 0;
    right: 0;
    top: 151px;
    text-align: center;
    font-family: "Cinzel", "Times New Roman", serif;
    font-size: 25px;
    line-height: 28px;
    letter-spacing: 0.6px;
    color: var(--back-text);
  }
</style>
</head>
<body>
<main class="canvas">
  <section class="card card--front" aria-label="Recto de la carte">
    <header class="holder">
      <h1 class="holder__name">MARIANNE LEBRODEL</h1>
      <p class="holder__role">HYPNOTHÉRAPEUTE</p>
    </header>
    <ul class="contact">
      <li class="contact__item">06 48 17 20 85</li>
      <li class="contact__item">47 rue des Tilleuls-Brunoy, 33710 Morvalle</li>
      <li class="contact__item">cabinet.lebrodel@velmoria.fr</li>
    </ul>
  </section>

  <section class="card card--back" aria-label="Verso de la carte">
    <div class="tree-motif" role="img" aria-label="Arbre de vie stylisé en filigrane : feuillage en haut, tronc et racines en bas"></div>
    <p class="practice">HYPNOTHERAPIE HUMANISTE<br>THERAPIE SYMBOLIQUE</p>
  </section>
</main>
</body>
</html>
```